Business Card Design for Cloud Frames

Hi we need a business card designed for a new aerial photography business we have started, we use UAV Drones to take photos for corporate, events, real estate, local government etc , the business name is Cloud Frames Australia, we have a facebook page that might help you come up with some designs - https://www.facebook.com/cloudframesaustralia

We need to have and editable AI file so that we can use different names and contact details. details for one of the cards as follow:

Dave Marsh
phone: 03 5512 4837
Mobile: 0439 175 286
email: dave@cloudframes.example.com.au
web: www.cloudframes.example.com.au

have now changed: Designer Payment:Committed

Target Market(s)

We are a Aerial Photography business using Drones and UAV

Industry/Entity Type

Business

Logo Text

Cloud Frames Australia

Requirements
Must have
• Colors to match logo and be part of Cloud Frames Brand

```html
<!DOCTYPE html>
<html lang="en">
<head>
<meta charset="utf-8">
<title>Cloud Frames Australia – Business Card</title>
<link rel="stylesheet" href="https://fonts.googleapis.com/css2?family=Quicksand:wght@400;600&display=swap">
<style>
  :root {
    --backdrop: #c8c8c8;
    --card-top: #35566c;
    --card-mid: #56798f;
    --card-low: #5e8298;
    --halo: rgba(214, 224, 232, 0.55);
    --halo-ring: rgba(225, 233, 240, 0.22);
    --ink: #1e2428;
    --ink-soft: #2c353b;
  }
  * { margin: 0; padding: 0; box-sizing: border-box; }
  html, body { width: 1200px; height: 873px; overflow: hidden; }
  body {
    background: var(--backdrop);
    font-family: "Quicksand", sans-serif;
    color: var(--ink);
  }
  .stage {
    position: relative;
    width: 1200px;
    height: 873px;
    display: flex;
    justify-content: center;
    align-items: center;
    gap: 80px;
  }
  .card {
    position: relative;
    width: 360px;
    height: 600px;
    overflow: hidden;
    background: linear-gradient(165deg, var(--card-top) 0%, var(--card-mid) 35%, var(--card-low) 100%);
    box-shadow: 0 18px 40px rgba(0, 0, 0, 0.25);
  }
  .card__halo {
    position: absolute;
    inset: 0;
    width: 100%;
    height: 100%;
  }
  /* Front */
  .brand-name {
    position: absolute;
    left: 0;
    right: 0;
    top: 205px;
    text-align: center;
    font-weight: 600;
    font-size: 38px;
    line-height: 1.1;
    letter-spacing: 1px;
    color: var(--ink);
  }
  .brand-name span { display: block; font-size: 20px; letter-spacing: 9px; margin-top: 8px; }
  .social {
    position: absolute;
    left: 46px;
    top: 448px;
    list-style: none;
  }
  .social__item {
    display: flex;
    align-items: center;
    gap: 9px;
    font-size: 13px;
    color: var(--ink-soft);
    height: 22px;
  }
  .social__mark {
    width: 13px;
    height: 13px;
    background: var(--ink-soft);
    opacity: 0.8;
  }
  /* Back */
  .person {
    position: absolute;
    left: 34px;
    top: 158px;
    font-size: 30px;
    font-weight: 400;
    color: var(--ink);
  }
  .contacts {
    position: absolute;
    left: 52px;
    top: 212px;
    list-style: none;
  }
  .contact {
    display: flex;
    align-items: center;
    gap: 20px;
    height: 44px;
    font-size: 13px;
    color: var(--ink-soft);
  }
  .contact__icon { width: 26px; height: 26px; flex: none; }
  .contact:first-child .contact__text { transform: translateY(-14px); }
</style>
</head>
<body>
<main class="stage">

  <section class="card card--front" aria-label="Card front">
    <svg class="card__halo" viewBox="0 0 360 600" aria-hidden="true">
      <circle cx="180" cy="250" r="225" fill="none" stroke="var(--halo-ring)" stroke-width="28"/>
      <circle cx="230" cy="330" r="250" fill="none" stroke="var(--halo-ring)" stroke-width="2"/>
      <circle cx="175" cy="245" r="175" fill="var(--halo)"/>
    </svg>
    <h1 class="brand-name">Cloud Frames<span>AUSTRALIA</span></h1>
    <ul class="social">
      <li class="social__item"><i class="social__mark"></i>facebook.com/cloudframesaustralia</li>
      <li class="social__item"><i class="social__mark"></i>@cloudframesaus</li>
      <li class="social__item"><i class="social__mark"></i>cloudframesaustralia</li>
    </ul>
  </section>

  <section class="card card--back" aria-label="Card back">
    <svg class="card__halo" viewBox="0 0 360 600" aria-hidden="true">
      <circle cx="150" cy="230" r="260" fill="none" stroke="var(--halo-ring)" stroke-width="30"/>
      <circle cx="240" cy="300" r="240" fill="none" stroke="var(--halo-ring)" stroke-width="2"/>
      <circle cx="175" cy="230" r="215" fill="var(--halo)"/>
    </svg>
    <h2 class="person">Dave Marsh</h2>
    <ul class="contacts">
      <li class="contact">
        <svg class="contact__icon" viewBox="0 0 26 26" aria-label="Phone">
          <rect x="3" y="8" width="20" height="16" rx="2" fill="var(--ink)"/>
          <rect x="5" y="2" width="5" height="8" rx="1.5" fill="var(--ink)"/>
          <rect x="13" y="11" width="8" height="3" fill="#6f8a9c"/>
          <g fill="#6f8a9c"><rect x="13" y="16" width="2" height="2"/><rect x="17" y="16" width="2" height="2"/><rect x="13" y="20" width="2" height="2"/><rect x="17" y="20" width="2" height="2"/></g>
        </svg>
        <span class="contact__text">03 5512 4837</span>
      </li>
      <li class="contact">
        <svg class="contact__icon" viewBox="0 0 26 26" aria-label="Mobile">
          <rect x="6" y="1" width="14" height="24" rx="3" fill="var(--ink)"/>
          <rect x="8" y="5" width="10" height="14" fill="#9fb2bf"/>
          <circle cx="13" cy="22" r="1.3" fill="#9fb2bf"/>
        </svg>
        <span class="contact__text">0439 175 286</span>
      </li>
      <li class="contact">
        <svg class="contact__icon" viewBox="0 0 26 26" aria-label="Email">
          <rect x="1" y="5" width="24" height="16" fill="var(--ink)"/>
          <path d="M1 5 L13 15 L25 5 M1 21 L10 12 M25 21 L16 12" fill="none" stroke="#9fb2bf" stroke-width="1.2"/>
        </svg>
        <span class="contact__text">dave@cloudframes.example.com.au</span>
      </li>
      <li class="contact">
        <svg class="contact__icon" viewBox="0 0 26 26" aria-label="Website">
          <circle cx="13" cy="13" r="11.5" fill="var(--ink)"/>
          <g fill="none" stroke="#9fb2bf" stroke-width="1">
            <ellipse cx="13" cy="13" rx="5" ry="11.5"/>
            <line x1="13" y1="1.5" x2="13" y2="24.5"/>
            <line x1="1.5" y1="13" x2="24.5" y2="13"/>
            <path d="M3.5 7 H22.5 M3.5 19 H22.5"/>
          </g>
        </svg>
        <span class="contact__text">www.cloudframes.example.com.au</span>
      </li>
    </ul>
  </section>

</main>
</body>
</html>
```